Keelbrook Vault Holdings Needs A Website

We are looking for a website for a new company. 4 Pages

Needs to be responsive and mobile friendly for all browsers and coded for both Android & IOS. SEO is also important.

Website Brief – Keelbrook Vault Holdings
Domain: www.keelbrookvault.net
Email: info@keelbrookvault.net
Phone: to be inserted later
Address: 40837 52 Ave, Edmonton, AB T6K 3R8
Platform: WordPress (recommended for flexibility, SEO tools, and ease of editing)
Requirements:
• Responsive & mobile-friendly (Android & iOS)
• Cross-browser compatibility
• Fast page load speed
• SEO optimized for storage development, management, and investment keywords
• Easy in-house editing after launch
• Professional, modern, trust-driven design reflecting expertise, reliability, and innovation
________________________________________
Pages
1. HOME
Purpose: Quickly communicate who Keelbrook Vault Holdings is and why they’re the best choice for designing, building, leasing, and managing self storage facilities.
Content Highlights:
• Hero Section: Large, bold image of a modern self storage facility with headline:
"From Concept to Capacity – Your Self Storage Experts"
• Subheadline: “Keelbrook Vault Holdings delivers turnkey design, construction, leasing, and management services for profitable self storage operations.”
• Quick Service Icons:
o Facility Design & Development
o Construction & Build Management
o Lease-Up & Marketing
o Ongoing Facility Management
• Call to Action Button: “LEARN MORE” → links to ABOUT US page.
• Featured Project Highlights: Showcase a few completed or current projects with photos and stats.
• Contact Banner: “Ready to build your next self storage project? Let’s talk.” → CONTACT page.
2. ABOUT US
Purpose: Build credibility, showcase experience, and explain the value proposition.
Content Highlights:
• Who We Are: Overview of Keelbrook Vault Holdings’ history, mission, and team expertise.
• Our Approach: End-to-end process from site selection to occupancy.
• Why Choose Us:
o Industry expertise in self storage
o Proven track record in lease-up success
o Strong vendor and contractor network
3. SERVICES
Purpose: Detail all service offerings with clarity and authority.
Sections:
• Design & Development: Market analysis, site planning, and architectural design.
• Construction Management: Overseeing timelines, budgets, and quality control.
• Lease-Up Strategy: Marketing, promotions, and occupancy acceleration.
• Ongoing Facility Management: Staffing, maintenance, revenue optimization.

4. CONTACT
Purpose: Provide simple, direct ways to connect.
Content Highlights:
• Contact Form (Name, Email, Phone, Message)
• Direct Email: info@keelbrookvault.net
• Phone (if applicable)
• Google Map embed (if there’s a head office location)
• CTA: “Let’s Build Your Storage Success Story.”
Design & Technical Notes
• Visual Style: Clean, modern, bold typography, professional color palette (to be based on branding), strong imagery of self storage facilities.
• Performance: Image compression, caching, responsive scaling.
• SEO Targets: “Self storage facility developer,” “self storage construction,” “self storage management company,” “lease-up services for self storage.”

WordPress or Joomla – must be desktop and mobile friendly with fast page load speed. Need the ability to edit ourselves.

Use pantone colours - #033c5a – dark blue
#2baadf – light blue

```html
<!DOCTYPE html>
<html lang="en">
<head>
<meta charset="utf-8">
<title>Keelbrook Vault Holdings – Self Storage Experts</title>
<link href="https://fonts.googleapis.com/css2?family=Montserrat:wght@300;400;500;600;700;800&display=swap" rel="stylesheet">
<style>
:root{
  --navy:#033c5a;
  --sky:#2baadf;
  --ink:#1f2a33;
  --muted:#6c747b;
  --paper:#f2f2f2;
  --paper-2:#e8e8e8;
  --white:#ffffff;
  --star:#f5b81c;
}
*{box-sizing:border-box;margin:0;padding:0}
html,body{width:1200px;height:4277px;overflow:hidden}
body{font-family:'Montserrat',sans-serif;color:var(--ink);background:var(--white);position:relative}
.abs{position:absolute}
a{color:inherit;text-decoration:none}

/* header */
.site-header{position:absolute;left:0;top:0;width:1200px;height:80px;background:var(--navy);border-bottom:1px solid rgba(255,255,255,.25)}
.brand{position:absolute;display:flex;align-items:center;gap:8px;color:var(--white)}
.brand-dot{width:34px;height:34px;background:var(--white);border-radius:50%}
.brand-name{font-weight:700;font-size:15px;line-height:1.05}
.brand-name small{display:block;font-weight:700;font-size:10px}
.main-nav{position:absolute;left:472px;top:32px;display:flex;gap:30px;font-size:11px;color:var(--white)}
.search-btn{position:absolute;left:1050px;top:22px;width:36px;height:36px;border-radius:50%;background:var(--sky)}

/* hero */
.hero-band{position:absolute;left:0;top:80px;width:1200px;height:290px;background:var(--navy)}
.hero-title{position:absolute;left:113px;top:130px;color:var(--white);font-size:49px;line-height:60px;font-weight:300}
.hero-title b{font-weight:800}
.hero-lead{position:absolute;left:753px;top:164px;width:330px;color:var(--white);font-size:12.5px;line-height:18px}
.pill{position:absolute;display:flex;align-items:center;justify-content:space-between;background:var(--sky);color:var(--white);border-radius:20px;font-size:10px;font-weight:700;letter-spacing:.3px;text-transform:uppercase;padding:0 8px 0 30px}
.hero-photo{position:absolute;left:0;top:370px;width:1200px;height:573px;background:linear-gradient(110deg,#d9c99a 0%,#7f98a6 30%,#5d7a88 55%,#2f4b58 100%)}

/* offer */
.offer{position:absolute;left:0;top:943px;width:1200px;height:912px;background:var(--paper)}
.section-title{position:absolute;font-size:32px;font-weight:400;color:var(--ink)}
.section-title b{font-weight:700}
.center{text-align:center}
.offer-lead{position:absolute;left:290px;top:1044px;width:620px;font-size:11.5px;line-height:17px;color:var(--muted);text-align:center}
.service-card{position:absolute;top:1110px;width:235px;height:273px;background:#e6e6e6;text-align:center;padding-top:24px}
.service-card.is-active{background:var(--sky);color:var(--white)}
.service-card svg{width:64px;height:64px}
.service-card h3{font-size:15px;font-weight:700;line-height:19px;margin-top:12px}
.service-card p{font-size:10px;line-height:14px;color:var(--muted);margin:6px 18px 0}
.service-card.is-active p{color:var(--white)}
.service-card .more{display:inline-block;margin-top:8px;font-size:10px;text-decoration:underline;color:var(--muted)}
.service-card.is-active .more{color:var(--white)}

/* who */
.who{position:absolute;left:113px;top:1445px;width:975px;height:348px;background:var(--white);box-shadow:0 4px 14px rgba(0,0,0,.1)}
.who-photo{position:absolute;left:17px;top:20px;width:476px;height:308px;background:linear-gradient(180deg,#b9b3a6 0%,#e4e6e8 35%,#c7ccd0 70%,#8f8a80 100%)}
.who-copy{position:absolute;left:538px;top:34px;width:400px}
.who-copy p{font-size:11.5px;line-height:16.5px;color:var(--muted);margin-top:14px}

/* projects */
.projects{position:absolute;left:0;top:1855px;width:1200px;height:945px;background:var(--paper-2)}
.proj-lead{position:absolute;left:589px;top:1917px;width:490px;font-size:11.5px;line-height:17px;color:var(--muted)}
.tile{position:absolute;width:312px;height:334px}

/* testimonials */
.clients{position:absolute;left:0;top:2800px;width:1200px;height:615px;background:var(--paper)}
.quote-name{position:absolute;left:672px;top:3027px;font-size:18px;font-weight:600}
.quote-role{position:absolute;left:672px;top:3052px;font-size:10px;color:#a0a6ab}
.stars{position:absolute;left:672px;top:3072px;display:flex;gap:5px}
.quote-text{position:absolute;left:672px;top:3105px;width:395px;font-size:11.5px;line-height:18px;color:var(--muted)}
.quote-mark{position:absolute;left:1003px;top:3000px;font-size:110px;font-weight:800;color:#7d8489;line-height:1}

/* banner */
.banner-photo{position:absolute;left:0;top:3415px;width:1200px;height:575px;background:linear-gradient(100deg,#2a2a2e 0%,#d96a52 30%,#8e8a86 55%,#4a5055 80%,#dfe2df 100%)}

/* footer */
.site-footer{position:absolute;left:0;top:3990px;width:1200px;height:287px;background:var(--navy);color:var(--white)}
.foot-nav{position:absolute;left:113px;top:4099px;display:flex;gap:42px;font-size:11px;color:var(--white)}
.foot-info{position:absolute;font-size:10.5px;color:var(--white);white-space:nowrap}
.foot-info b{font-weight:700}
.cta-title{position:absolute;left:690px;top:4064px;font-size:16px;font-weight:700;color:var(--white)}
.cta-sub{position:absolute;left:690px;top:4094px;font-size:10px;color:var(--white);opacity:.85}
.foot-rule{position:absolute;left:0;top:4212px;width:1200px;height:1px;background:rgba(255,255,255,.35)}
.copyright{position:absolute;left:111px;top:4242px;font-size:10px;color:var(--white);opacity:.85}
.contact-icon{position:absolute;top:4234px;width:26px;height:26px;border-radius:50%;background:var(--sky);display:flex;align-items:center;justify-content:center}
</style>
</head>
<body>

<header class="site-header">
  <div class="brand" style="left:113px;top:22px">
    <span class="brand-dot"></span>
    <span class="brand-name">Keelbrook Vault<small>Holdings</small></span>
  </div>
  <nav class="main-nav"><a>About Us</a><a>service</a><a>Projects</a><a>Contact</a></nav>
  <div class="search-btn">
    <svg width="36" height="36" viewBox="0 0 36 36"><circle cx="17" cy="17" r="5" fill="none" stroke="#fff" stroke-width="1.5"/><line x1="20.5" y1="20.5" x2="24" y2="24" stroke="#fff" stroke-width="1.5"/></svg>
  </div>
</header>

<section class="hero-band"></section>
<h1 class="hero-title"><b>From Concept to<br>Capacity –</b> Your Self<br>Storage Experts</h1>
<p class="hero-lead">Keelbrook Vault Holdings delivers turnkey design, construction, leasing, and management services for profitable self storage operations.</p>
<a class="pill" style="left:754px;top:242px;width:172px;height:38px">Learn More
  <svg width="32" height="32" viewBox="0 0 32 32"><circle cx="16" cy="16" r="14" fill="var(--navy)"/><path d="M8 16h15M19 11l5 5-5 5" stroke="#fff" stroke-width="1.6" fill="none"/></svg>
</a>

<div class="hero-photo" role="img" aria-label="Modern self storage facility with glass entrance and city towers"></div>

<section class="offer"></section>
<h2 class="section-title center" style="left:0;top:995px;width:1200px">What We <b>Offer</b></h2>
<p class="offer-lead">Lorem ipsum dolor sit amet, consectetur adipiscing elit, sed do eiusmod tempor incididunt ut labore et dolore magna aliqua. Quis ipsum suspendisse ultrices gravida.</p>

<article class="service-card" style="left:113px">
  <svg viewBox="0 0 64 64" fill="none" stroke="var(--sky)" stroke-width="2.5"><rect x="10" y="8" width="44" height="48"/><path d="M10 40h18v16M40 8v20h14"/></svg>
  <h3>Facility Design &amp;<br>Development</h3>
  <p>Lorem ipsum dolor sit amet, consectetur adipiscing elit, sed do eiusmod tempor incididunt ut labore et dolore magna aliqua.</p>
  <a class="more">Learn More</a>
</article>
<article class="service-card is-active" style="left:360px">
  <svg viewBox="0 0 64 64" fill="none" stroke="#fff" stroke-width="2.5"><path d="M12 44a20 20 0 0 1 40 0"/><rect x="6" y="44" width="52" height="8"/><path d="M26 26v-8h12v8M32 18v26"/></svg>
  <h3>Construction &amp;<br>Build Management</h3>
  <p>Lorem ipsum dolor sit amet, consectetur adipiscing elit, sed do eiusmod tempor incididunt ut labore et dolore magna aliqua.</p>
  <a class="more">Learn More</a>
</article>
<article class="service-card" style="left:607px">
  <svg viewBox="0 0 64 64" fill="none" stroke="var(--sky)" stroke-width="2.5"><path d="M10 30l30-16v34L10 38z"/><path d="M18 40l4 14h6l-3-12M46 24h8M44 16l6-5M44 34l6 5"/></svg>
  <h3>Lease-Up &amp;<br>Marketing</h3>
  <p>Lorem ipsum dolor sit amet, consectetur adipiscing elit, sed do eiusmod tempor incididunt ut labore et dolore magna aliqua.</p>
  <a class="more">Learn More</a>
</article>
<article class="service-card" style="left:854px">
  <svg viewBox="0 0 64 64" fill="none" stroke="var(--sky)" stroke-width="2.5"><circle cx="32" cy="32" r="18" stroke-dasharray="7 4"/><circle cx="32" cy="32" r="8"/></svg>
  <h3>Ongoing Facility<br>Management</h3>
  <p>Lorem ipsum dolor sit amet, consectetur adipiscing elit, sed do eiusmod tempor incididunt ut labore et dolore magna aliqua.</p>
  <a class="more">Learn More</a>
</article>

<section class="who">
  <div class="who-photo" role="img" aria-label="Empty storage warehouse interior with loading doors"></div>
  <div class="who-copy">
    <h2 style="font-size:32px;font-weight:400"><b>Who</b> We Are</h2>
    <p style="margin-top:20px">Our mission is simple: to be your trusted partner in building, leasing, and operating modern storage solutions that succeed in today’s competitive market.</p>
    <p>At Keelbrook Vault Holdings, we specialize in turning vision into reality for self storage investors, developers, and operators. Based in Edmonton, Alberta, we bring together decades of combined expertise in design, construction, leasing, and management to create self storage facilities that deliver long-term profitability.</p>
  </div>
  <a class="pill" style="left:538px;top:259px;width:176px;height:38px;padding-left:18px;font-size:9.5px">View Our Works
    <svg width="32" height="16" viewBox="0 0 32 16"><path d="M4 8h22M21 3l5 5-5 5" stroke="#fff" stroke-width="1.5" fill="none"/></svg>
  </a>
</section>

<section class="projects"></section>
<h2 class="section-title" style="left:111px;top:1912px;line-height:36px"><b>Projects</b> That Deliver<br>Results</h2>
<p class="proj-lead">Lorem ipsum dolor sit amet, consectetur adipiscing elit, sed do eiusmod tempor incididunt ut labore et dolore magna aliqua.</p>
<a class="pill" style="left:592px;top:1965px;width:176px;height:38px;padding-left:18px;font-size:9.5px">View Our Works
  <svg width="32" height="16" viewBox="0 0 32 16"><path d="M4 8h22M21 3l5 5-5 5" stroke="#fff" stroke-width="1.5" fill="none"/></svg>
</a>
<div class="tile" style="left:113px;top:2046px;background:linear-gradient(90deg,#5d9a3a,#c9d3d2 55%,#eef0f0)" role="img" aria-label="Corridor of green self storage unit doors"></div>
<div class="tile" style="left:445px;top:2046px;background:linear-gradient(180deg,#e6e3dd 0%,#d6d2cb 40%,#6c6a66 62%,#b3aca2 100%)" role="img" aria-label="Roll-up storage door in a bright interior"></div>
<div class="tile" style="left:777px;top:2046px;background:linear-gradient(90deg,#2f5c9a,#d8d8d6 50%,#c5a93b 85%,#dcdcdc)" role="img" aria-label="Warehouse aisle with tall blue racking"></div>
<div class="tile" style="left:113px;top:2402px;background:linear-gradient(180deg,#e3e4e3,#b79c7c 50%,#8a7560)" role="img" aria-label="Stacked wrapped pallets of boxes"></div>
<div class="tile" style="left:445px;top:2402px;background:linear-gradient(120deg,#4a4a48,#a9aaa8 50%,#5b5b58)" role="img" aria-label="Row of corrugated metal storage doors"></div>
<div class="tile" style="left:777px;top:2402px;background:linear-gradient(150deg,#6e5443,#b88a62 45%,#3b3633)" role="img" aria-label="Storage office desk with lamp and boxes"></div>

<section class="clients"></section>
<div class="abs" style="left:113px;top:2862px;width:435px;height:465px;background:linear-gradient(100deg,#c9d2d4,#e7c96a 55%,#6d8f99)" role="img" aria-label="Glass facade of a modern building at sunset"></div>
<div class="abs" style="left:357px;top:3085px;width:248px;height:267px;background:linear-gradient(180deg,#b5b3ac 0%,#2f4a52 35%,#4f7b7f 75%,#d9d9d6 100%);box-shadow:0 4px 14px rgba(0,0,0,.15)" role="img" aria-label="Dark glass storefront of a storage facility"></div>
<h2 class="section-title" style="left:672px;top:2933px"><b>What</b> Clients Say</h2>
<p class="quote-name">MARLENE</p>
<p class="quote-role">Pharmacist</p>
<div class="stars">
  <svg width="100" height="18" viewBox="0 0 100 18" fill="var(--star)">
    <polygon points="9,1 11.4,6.6 17.5,7 12.8,11 14.3,17 9,13.8 3.7,17 5.2,11 0.5,7 6.6,6.6"/>
    <polygon transform="translate(21 0)" points="9,1 11.4,6.6 17.5,7 12.8,11 14.3,17 9,13.8 3.7,17 5.2,11 0.5,7 6.6,6.6"/>
    <polygon transform="translate(42 0)" points="9,1 11.4,6.6 17.5,7 12.8,11 14.3,17 9,13.8 3.7,17 5.2,11 0.5,7 6.6,6.6"/>
    <polygon transform="translate(63 0)" points="9,1 11.4,6.6 17.5,7 12.8,11 14.3,17 9,13.8 3.7,17 5.2,11 0.5,7 6.6,6.6"/>
    <polygon transform="translate(84 0)" points="9,1 11.4,6.6 17.5,7 12.8,11 14.3,17 9,13.8 3.7,17 5.2,11 0.5,7 6.6,6.6"/>
  </svg>
</div>
<span class="quote-mark">”</span>
<p class="quote-text">“Lorem ipsum dolor sit amet, consectetur adipiscing elit, sed do eiusmod tempor incididunt ut labore et dolore magna aliqua. Quis ipsum suspendisse ultrices gravida. Risus commodo viverra maecenas accumsan lacus vel facilisis. ”</p>
<svg class="abs" style="left:670px;top:3234px" width="60" height="16" viewBox="0 0 60 16">
  <path d="M26 8H4M9 3L4 8l5 5" stroke="var(--ink)" stroke-width="1.5" fill="none"/>
  <path d="M34 8h22M51 3l5 5-5 5" stroke="var(--sky)" stroke-width="1.5" fill="none"/>
</svg>

<div class="banner-photo" role="img" aria-label="Storage facility lobby with red ceiling and glass walls"></div>

<footer class="site-footer"></footer>
<div class="brand" style="left:113px;top:4034px">
  <span class="brand-dot"></span>
  <span class="brand-name">Keelbrook Vault<small>Holdings</small></span>
</div>
<nav class="foot-nav"><a>About Us</a><a>service</a><a>Projects</a><a>Contact</a></nav>
<p class="foot-info" style="left:111px;top:4131px"><b>Address:</b> 40837 52 Ave, Edmonton, AB T6K 3R8</p>
<p class="foot-info" style="left:390px;top:4131px"><b>Email:</b> info@keelbrookvault.net</p>
<p class="foot-info" style="left:111px;top:4160px"><b>Phone:</b> 780 555 0142</p>
<p class="cta-title">Ready to build your next self storage project?</p>
<p class="cta-sub">Let’s talk about your vision today.</p>
<a class="pill" style="left:691px;top:4125px;width:152px;height:36px;padding-left:22px;font-size:9.5px">Contact Us
  <svg width="32" height="16" viewBox="0 0 32 16"><path d="M4 8h22M21 3l5 5-5 5" stroke="#fff" stroke-width="1.5" fill="none"/></svg>
</a>
<div class="foot-rule"></div>
<p class="copyright">Copyright © 2025. All rights reserved.</p>
<span class="contact-icon" style="left:942px" aria-label="Email">
  <svg width="14" height="14" viewBox="0 0 14 14" fill="none" stroke="#fff" stroke-width="1.3"><rect x="1.5" y="3" width="11" height="8"/><path d="M1.5 3l5.5 4.5L12.5 3"/></svg>
</span>
<span class="contact-icon" style="left:982px" aria-label="Phone">
  <svg width="14" height="14" viewBox="0 0 14 14" fill="none" stroke="#fff" stroke-width="1.3"><path d="M3 1.5h2.5l1 3-1.5 1a7 7 0 0 0 3.5 3.5l1-1.5 3 1V11a1.5 1.5 0 0 1-1.5 1.5A10 10 0 0 1 1.5 3 1.5 1.5 0 0 1 3 1.5z"/></svg>
</span>
<span class="contact-icon" style="left:1022px" aria-label="Location">
  <svg width="14" height="14" viewBox="0 0 14 14" fill="none" stroke="#fff" stroke-width="1.3"><path d="M7 13s4-4.2 4-7.2a4 4 0 0 0-8 0C3 8.8 7 13 7 13z"/><circle cx="7" cy="5.8" r="1.4"/></svg>
</span>
<span class="contact-icon" style="left:1062px" aria-label="Back to top">
  <svg width="14" height="14" viewBox="0 0 14 14" fill="none" stroke="#fff" stroke-width="1.3"><path d="M7 12V2M3 6l4-4 4 4"/></svg>
</span>

</body>
</html>
```